Brookhaven Business Card

I would like to re-design my company business card. I have my main company logo (Brookhaven) which must remain unchanged and I also have a number of product brands which I would like to also show on the card in some way. The corporate company colors are Blue and Orange, see pantone colors on file. However, it is not necessary to use these colors thoroughout. I am ok with grey tones etc...

Target Market(s)

Trade Business

Industry/Entity Type

Furniture

Contact Information for Business Card

Needs to incorporate Brookhaven as the main Logo. The Torvel and Kandrel product brands within the company. These can be on the back of the card.

Font styles to use
Sans Serif

Colors
0355a3
f37122

Requirements
Must have
• Marco Velditch
• COO (Global)
• Brookhaven Pacific Holdings Inc. (4371)
• Level 3, 47 Harlow Street, Melbourne VIC 3000 Australia
• Tel: +61 3 9481 2736 Mobile: +61 427 586 204
• e-mail: marco@brookhaven-au.example
• web: www.brookhaven-au.example
Nice to have
• Should be a corporate
Should not have
• No images of furniture

```html
<!DOCTYPE html>
<html lang="en">
<head>
<meta charset="utf-8">
<title>Brookhaven Business Card</title>
<link rel="stylesheet" href="https://fonts.googleapis.com/css2?family=Roboto:wght@400;700&display=swap">
<style>
  :root {
    --backdrop: #ece9e4;
    --card: #ffffff;
    --brand-blue: #0355a3;
    --name-blue: #1f4fd8;
    --brand-orange: #f37122;
    --ink: #222222;
    --ink-soft: #3a3a3a;
  }
  * { margin: 0; padding: 0; box-sizing: border-box; }
  html, body {
    width: 1200px; height: 1000px; overflow: hidden;
    background: var(--backdrop);
    font-family: "Roboto", Arial, sans-serif;
  }
  .canvas { position: relative; width: 1200px; height: 1000px; }
  .card {
    position: absolute; width: 760px; height: 434px;
    background: var(--card);
    box-shadow: 0 6px 18px rgba(0,0,0,0.18);
  }
  .card--brand { left: 80px; top: 60px; }
  .card--contact { left: 360px; top: 520px; }

  .product-mark {
    position: absolute; left: 90px; top: 130px;
    color: var(--ink); font-weight: 700; line-height: 1;
  }
  .product-mark__name { font-size: 118px; letter-spacing: 2px; }
  .product-mark__owner { font-size: 40px; margin: 8px 0 0 210px; }

  .company-mark {
    position: absolute; left: 50px; top: 60px;
    display: flex; align-items: center; gap: 36px;
  }
  .company-mark__square {
    width: 120px; height: 120px;
    border: 6px solid var(--brand-orange); border-radius: 14px;
  }
  .company-mark__name {
    color: var(--name-blue); font-weight: 700; font-size: 88px; letter-spacing: -1px;
  }

  .person { position: absolute; left: 50px; top: 250px; }
  .person__name { color: var(--name-blue); font-weight: 700; font-size: 21px; }
  .person__role { color: var(--name-blue); font-size: 17px; margin-top: 4px; }
  .contact-list { list-style: none; margin-top: 12px; }
  .contact-list li {
    display: flex; align-items: center; gap: 12px;
    font-size: 17px; color: var(--ink); line-height: 24px;
  }
  .contact-list svg { width: 12px; height: 12px; fill: var(--ink-soft); }

  .address {
    position: absolute; right: 40px; top: 250px;
    font-size: 16px; line-height: 22px; color: var(--ink-soft);
  }
</style>
</head>
<body>
<main class="canvas">
  <section class="card card--brand" aria-label="Card front, product brand">
    <div class="product-mark">
      <div class="product-mark__name">TORVEL</div>
      <div class="product-mark__owner">by Brookhaven</div>
    </div>
  </section>

  <section class="card card--contact" aria-label="Card back, contact details">
    <div class="company-mark">
      <span class="company-mark__square" aria-hidden="true"></span>
      <span class="company-mark__name">Brookhaven</span>
    </div>

    <div class="person">
      <p class="person__name">Marco Velditch</p>
      <p class="person__role">COO (Global)</p>
      <ul class="contact-list">
        <li><svg viewBox="0 0 12 12"><path d="M2.5 0.5l2 2-1 1.5c.6 1.6 1.9 2.9 3.5 3.5l1.5-1 2 2-1.5 2C4.5 12 0 7.5 0.5 2z"/></svg>+61 3 9481 2736</li>
        <li><svg viewBox="0 0 12 12"><path d="M3 0h6v12H3zM4 1.5v8h4v-8z"/></svg>+61 427 586 204</li>
        <li><svg viewBox="0 0 12 12"><path d="M0 2h12v8H0zM1 3l5 3.5L11 3z"/></svg>marco@brookhaven-au.example</li>
        <li><svg viewBox="0 0 12 12"><circle cx="6" cy="6" r="5.5"/></svg>www.brookhaven-au.example</li>
      </ul>
    </div>

    <address class="address" style="font-style:normal">
      Brookhaven Pacific Holdings Inc. (4371)<br>
      Level 3, 47 Harlow Street, Melbourne<br>
      VIC 3000 Australia
    </address>
  </section>
</main>
</body>
</html>
```